Business Cards for our company

Hi there,

we have successfully designed a logo with ArtFlock and would like now to design our business cards. We would like to keep the colours and the look-and-feel of the logo. Please send in variations with two or three colours and one or two sides. I promise to respond to every single submission.

Many thanks and happy new year.

All the best,
Wilfried

Target Market(s)

B2B

Industry/Entity Type

Trade

Contact Information for Business Card

We have successfully designed a logo with ArtFlock and would like now to design our business cards. We would like to keep the colours and the look-and-feel of the logo. Please send in variations with two or three colours and one or two sides. I promise to respond to every single submission.

Font styles to use
Serif
Sans Serif
Script

Requirements
Must have
• These information should be on the business card, grouped as you suggest, and we think using small pictograms for mobile, email, etc is pretty helpful:
• Wilfried Tammler (first and second name)
• Geschäftsführer/ Managing Director (title)
• KoR Warenkontor GmbH (company name and legal form)
• Ostheimer Str. 18/3 (street and house number)
• 70839 Gerlingen (zip code and town)
• +491709384562 (mobile)
• +4971569027341 (work)
• w.tammler@kor-warenkontor.example (email)
• www.kor-warenkontor.example (web)
Nice to have
• Spectacular and interesting layout and design. You look at it and think, wow, that's not the normal stuff.
• We think of ourselves as bridge-builders between businesses (international producers on the one hand, and retail chains on the other hand) and we translate, organise and manage projects where both partners are involved, but it's difficult for them to cooperate due to language barriers and different working cultures.
• This is why we have the n between the B's shaped as a bridge, and the green arc supports this idea. Maybe you could play with this idea...
Should not have
• the standard layout that everybody has

```html
<!DOCTYPE html>
<html lang="en">
<head>
<meta charset="utf-8">
<title>KoR Warenkontor – Business Card</title>
<link rel="stylesheet" href="https://fonts.googleapis.com/css2?family=Cinzel:wght@400;700&family=Playfair+Display:wght@700&display=swap">
<style>
  :root {
    --bg: #6b6a6a;
    --card: #ffffff;
    --ink: #111111;
    --green: #2faa4a;
    --rule: #222222;
  }
  * { margin: 0; padding: 0; box-sizing: border-box; }
  html, body { width: 1200px; height: 900px; overflow: hidden; }
  body { background: var(--bg); position: relative; }
  .card {
    position: absolute; left: 75px; top: 150px;
    width: 1050px; height: 600px;
    background: var(--card); overflow: hidden;
    font-family: "Cinzel", serif; color: var(--ink);
  }
  .swoosh { position: absolute; inset: 0; width: 1050px; height: 600px; }
  .brand {
    position: absolute; left: 70px; top: 215px;
    display: flex; align-items: center; gap: 16px;
  }
  .brand-dot { width: 26px; height: 26px; border-radius: 50%; background: var(--green); }
  .brand-name { font-family: "Cinzel", serif; font-weight: 700; font-size: 38px; line-height: 1.1; color: var(--ink); }
  .divider { position: absolute; left: 440px; top: 110px; width: 2px; height: 220px; background: var(--rule); }
  .details { position: absolute; left: 480px; top: 40px; }
  .person-name { font-family: "Playfair Display", serif; font-weight: 700; font-size: 40px; line-height: 1.2; letter-spacing: 1px; text-transform: uppercase; }
  .person-title { color: var(--green); font-size: 19px; line-height: 1.2; margin-left: 10px; text-transform: uppercase; }
  .company { margin-top: 28px; margin-left: 50px; font-size: 17px; line-height: 1.25; text-transform: uppercase; }
  .contacts { list-style: none; margin-top: 16px; margin-left: 50px; font-size: 17px; line-height: 1.4; }
  .contacts li { display: flex; align-items: center; gap: 12px; text-transform: uppercase; }
  .contacts svg { width: 18px; height: 18px; flex: none; }
</style>
</head>
<body>
  <div class="card">
    <svg class="swoosh" viewBox="0 0 1050 600" aria-hidden="true">
      <path d="M0,490 Q600,490 1050,360 L1050,600 L0,600Z" fill="#2faa4a"/>
      <path d="M0,500 Q605,500 1050,372 L1050,600 L0,600Z" fill="#ffffff"/>
      <path d="M0,508 Q610,508 1050,380 L1050,600 L0,600Z" fill="#2faa4a"/>
      <path d="M0,518 Q615,516 1050,392 L1050,600 L0,600Z" fill="#ffffff"/>
      <path d="M0,528 Q620,524 1050,400 L1050,600 L0,600Z" fill="#111111"/>
      <path d="M420,600 Q860,560 1050,420 L1050,600Z" fill="#ffffff"/>
      <path d="M440,600 Q870,565 1050,428 L1050,600Z" fill="#2faa4a"/>
    </svg>

    <div class="brand">
      <span class="brand-dot"></span>
      <span class="brand-name">KoR<br>Warenkontor</span>
    </div>

    <div class="divider"></div>

    <div class="details">
      <h1 class="person-name">Wilfried Tammler</h1>
      <p class="person-title">Managing Director</p>
      <p class="company">KoR Warenkontor GmbH<br>Ostheimer Str.18/3<br>70839 Gerlingen</p>
      <ul class="contacts">
        <li><svg viewBox="0 0 24 24"><path fill="#2faa4a" d="M6.6 10.8a15 15 0 0 0 6.6 6.6l2.2-2.2c.3-.3.7-.4 1-.2 1.1.4 2.3.6 3.6.6.6 0 1 .4 1 1V20c0 .6-.4 1-1 1A17 17 0 0 1 3 4c0-.6.4-1 1-1h3.5c.6 0 1 .4 1 1 0 1.3.2 2.5.6 3.6.1.3 0 .7-.2 1z"/></svg>+491709384562</li>
        <li><svg viewBox="0 0 24 24"><rect x="6" y="2" width="12" height="20" rx="2" fill="none" stroke="#2faa4a" stroke-width="2"/><circle cx="12" cy="18" r="1.3" fill="#2faa4a"/></svg>+4971569027341</li>
        <li><svg viewBox="0 0 24 24"><circle cx="12" cy="12" r="4" fill="none" stroke="#2faa4a" stroke-width="2.5"/><path d="M16 8v5a3 3 0 0 0 6 0v-1a10 10 0 1 0-4 8" fill="none" stroke="#2faa4a" stroke-width="2.5"/></svg>w.tammler@kor-warenkontor.example</li>
        <li><svg viewBox="0 0 24 24"><circle cx="12" cy="12" r="10" fill="#2faa4a"/><path d="M2 12h20M12 2c3 3 3 17 0 20M12 2c-3 3-3 17 0 20" fill="none" stroke="#fff" stroke-width="1.2"/></svg>www.kor-warenkontor.example</li>
      </ul>
    </div>
  </div>
</body>
</html>
```